Stationary and design update for my brand

I need new letterhead, a new business card, business envelope design, new keynote and powerpoint branded slides (16x9). I have logo samples in various styles and brand standards for fonts and colors.

Font styles to use
Sans Serif

```html
<!DOCTYPE html>
<html lang="en">
<head>
<meta charset="utf-8">
<title>Crestline Coaching – Business Card</title>
<link href="https://fonts.googleapis.com/css2?family=Jost:wght@400;500&family=Noto+Serif:wght@700&display=swap" rel="stylesheet">
<style>
  :root {
    --backdrop: #3b332f;
    --card-white: #fbfbfb;
    --card-grey: #7d7e80;
    --orange: #ee8d1f;
    --charcoal: #4d4d4f;
    --ink: #3a3a3c;
    --emboss: #5c5d60;
  }
  * { margin: 0; padding: 0; box-sizing: border-box; }
  html, body { width: 1200px; height: 716px; overflow: hidden; }
  body {
    background: var(--backdrop);
    position: relative;
    font-family: "Jost", sans-serif;
  }
  .card {
    position: absolute;
    top: 208px;
    width: 525px;
    height: 300px;
    overflow: hidden;
    box-shadow: 0 10px 24px rgba(0,0,0,.45);
  }
  .card--back {
    left: 45px;
    background: var(--card-grey);
    display: flex;
    align-items: center;
    justify-content: center;
  }
  .card--back .brand-name {
    color: var(--emboss);
    font-size: 40px;
    font-weight: 500;
    letter-spacing: 4px;
  }
  .card--front {
    left: 630px;
    background: var(--card-white);
  }
  .contact {
    position: absolute;
    left: 28px;
    top: 26px;
    color: var(--ink);
  }
  .contact__name {
    font-family: "Noto Serif", serif;
    font-weight: 700;
    color: var(--orange);
    font-size: 17px;
  }
  .contact__name small { font-size: 11px; }
  .contact__roles { font-size: 11.5px; margin-top: 2px; }
  .contact__org { font-size: 11.5px; margin-top: 10px; line-height: 1.35; }
  .contact__lines { list-style: none; margin-top: 10px; font-size: 11.5px; line-height: 1.45; }
  .contact__lines li { display: flex; align-items: center; gap: 6px; }
  .contact__lines svg { width: 10px; height: 10px; flex: none; }
  .card--front .brand-name {
    position: absolute;
    right: 34px;
    top: 128px;
    color: var(--orange);
    font-size: 26px;
    font-weight: 500;
    letter-spacing: 2px;
  }
  .mountain-art {
    position: absolute;
    left: 0; right: 0; bottom: 0;
    height: 118px;
    background: linear-gradient(160deg, var(--orange) 0%, var(--orange) 28%, var(--charcoal) 45%, var(--charcoal) 80%, var(--orange) 100%);
  }
</style>
</head>
<body>
  <section class="card card--back">
    <span class="brand-name">CRESTLINE COACHING</span>
  </section>

  <section class="card card--front">
    <div class="contact">
      <h1 class="contact__name">Daniel Ashworth-Kemp, <small>DMIN, PCC</small></h1>
      <p class="contact__roles">Owner | Trainer | Coach | Consultant</p>
      <p class="contact__org">Crestline Coaching &amp; Behavioral Consulting LLC<br>2468 Larkspur Dr. Fairview, TX 75069</p>
      <ul class="contact__lines">
        <li><svg viewBox="0 0 10 10"><rect x="2.5" y="0.5" width="5" height="9" rx="1" fill="none" stroke="#ee8d1f" stroke-width="1.2"/></svg>(555) 014-2290</li>
        <li><svg viewBox="0 0 10 10"><rect x="0.5" y="2" width="9" height="6.5" fill="#ee8d1f"/><path d="M0.5 2 L5 5.5 L9.5 2" fill="none" stroke="#fff" stroke-width="1"/></svg>daniel@crestlinecbc.com</li>
        <li><svg viewBox="0 0 10 10"><circle cx="5" cy="5" r="4.5" fill="#ee8d1f"/><path d="M0.5 5 H9.5 M5 0.5 C2.5 3 2.5 7 5 9.5 M5 0.5 C7.5 3 7.5 7 5 9.5" fill="none" stroke="#fff" stroke-width="0.7"/></svg>www.crestlinecbc.com</li>
      </ul>
    </div>
    <span class="brand-name">CRESTLINE COACHING</span>
    <div class="mountain-art" role="img" aria-label="Stylised orange and charcoal mountain range illustration along the bottom of the card"></div>
  </section>
</body>
</html>
```